Wattlegrove Campus Lodgings needs a business card design

Hi Guys,

We are a Student Accommodation company in Australia. We already have a logo which I will submit.

I will require the design of the business cards from you.

I am after something that looks clean, modern and that people feel interested and actually want to contact us.

We would like to see designs that are innovative.

On the business cards I will require to have:

Employee Name
Position
Phone number
Email
Facebook page

I hope you can help me with this project guys as I have heard really good things from you.

```html
<!DOCTYPE html>
<html lang="en">
<head>
<meta charset="utf-8">
<title>Wattlegrove Campus Lodgings — Business Card</title>
<link href="https://fonts.googleapis.com/css2?family=Lato:wght@300;400;700;900&display=swap" rel="stylesheet">
<style>
  :root {
    --backdrop: #3a3a3c;
    --card-yellow: #ffc336;
    --card-black: #050505;
    --ink: #161616;
    --ink-soft: #2b2b2b;
    --brand-grey: #5a5a5a;
    --brand-yellow: #f2b733;
    --url-grey: #8a8a8a;
  }
  * { box-sizing: border-box; margin: 0; padding: 0; }
  html, body {
    width: 1200px; height: 926px; overflow: hidden;
    background: var(--backdrop);
    font-family: "Lato", Arial, sans-serif;
  }
  .canvas { position: relative; width: 1200px; height: 926px; }

  .card {
    position: absolute;
    width: 640px; height: 366px;
    border-radius: 3px;
    box-shadow: 0 12px 28px rgba(0,0,0,.45);
  }

  /* Back side */
  .card-back { left: 480px; top: 70px; background: var(--card-black); }
  .card-back .brand {
    position: absolute; left: 0; right: 0; top: 120px;
    display: flex; justify-content: center; align-items: center; gap: 12px;
  }
  .card-back .brand-square { width: 34px; height: 34px; background: var(--brand-yellow); }
  .card-back .brand-name {
    color: var(--brand-yellow); font-weight: 900; font-size: 24px;
    line-height: 1.05; text-transform: uppercase; letter-spacing: .5px; width: 200px;
  }
  .card-back .social-url {
    position: absolute; left: 40px; right: 40px; top: 262px;
    color: var(--url-grey); font-weight: 400; font-size: 15px; letter-spacing: 1px;
    white-space: nowrap;
  }

  /* Front side */
  .card-front { left: 70px; top: 480px; background: var(--card-yellow); color: var(--ink); }
  .card-front .brand {
    position: absolute; left: 42px; top: 146px;
    display: flex; align-items: center; gap: 12px;
  }
  .card-front .brand-square { width: 30px; height: 30px; background: var(--brand-grey); }
  .card-front .brand-name {
    color: var(--brand-grey); font-weight: 900; font-size: 20px;
    line-height: 1.05; text-transform: uppercase; width: 170px;
  }
  .identity { position: absolute; left: 318px; top: 86px; }
  .person-name { font-size: 38px; line-height: 1; letter-spacing: .3px; }
  .person-name .first { font-weight: 300; }
  .person-name .last { font-weight: 700; }
  .person-title { font-size: 11px; font-weight: 400; letter-spacing: .4px; margin-top: 4px; text-transform: uppercase; }

  .contacts { position: absolute; left: 318px; top: 168px; list-style: none; }
  .contacts li {
    display: flex; align-items: flex-start; gap: 10px;
    font-size: 17px; line-height: 26px; color: var(--ink-soft); letter-spacing: .4px;
  }
  .contacts li.address { margin-top: 6px; line-height: 24px; }
  .contacts svg { width: 13px; height: 13px; flex: none; margin-top: 6px; fill: var(--ink); }
</style>
</head>
<body>
<main class="canvas">

  <section class="card card-back" aria-label="Business card back">
    <div class="brand">
      <span class="brand-square"></span>
      <span class="brand-name">Wattlegrove Campus Lodgings</span>
    </div>
    <p class="social-url">chatterhub.net/pages/Wattlegrove-Campus-Lodgings/482017365019</p>
  </section>

  <section class="card card-front" aria-label="Business card front">
    <div class="brand">
      <span class="brand-square"></span>
      <span class="brand-name">Wattlegrove Campus Lodgings</span>
    </div>

    <div class="identity">
      <h1 class="person-name"><span class="first">John</span> <span class="last">Smith</span></h1>
      <p class="person-title">Title goes here</p>
    </div>

    <ul class="contacts">
      <li>
        <svg viewBox="0 0 16 16" aria-hidden="true"><path d="M3.6 1.2 6 3.6 4.6 5.6c.9 2.3 3.5 4.9 5.8 5.8l2-1.4 2.4 2.4-1.8 2.2C7.5 14.6 1.4 8.5 1.4 3z"/></svg>
        <span>123-456-7890</span>
      </li>
      <li>
        <svg viewBox="0 0 16 16" aria-hidden="true"><path d="M1 3h14v1.2L8 9 1 4.2zM1 6l7 4.8L15 6v7H1z"/></svg>
        <span>yourdomain.com</span>
      </li>
      <li>
        <svg viewBox="0 0 16 16" aria-hidden="true"><path d="M6.5 9.5 9.5 6.5l1 1-3 3zM4 9l-1.6 1.6a2.1 2.1 0 0 0 3 3L7 12l1 1-1.6 1.6a3.5 3.5 0 0 1-5-5L3 8zm8-2 1.6-1.6a2.1 2.1 0 0 0-3-3L9 4 8 3l1.6-1.6a3.5 3.5 0 0 1 5 5L13 8z"/></svg>
        <span>yourname@yourdomain.com</span>
      </li>
      <li class="address">
        <svg viewBox="0 0 16 16" aria-hidden="true"><path d="M8 1.5 15 8h-2v6.5H9.5V10h-3v4.5H3V8H1z"/></svg>
        <span>Street address goes here,<br>Suite #303, Alt Bldg, NY 82365</span>
      </li>
    </ul>
  </section>

</main>
</body>
</html>
```